Need a business card design for a new business

The business is going to be called "The Maple Lectern" - it is an online training company that provides Instructor Lead training to students at any destination in the world
The reference to cloud is the internet and classroom reference will be a computer at the students and instructors end

We will need a Web site and stationary and advertising material developed over time but for now require the business cards only

So if we are happy with the business card then we will use the same designers for the other requirments of the business as it evolves

Industry/Entity Type

Advertising

```html
<!DOCTYPE html>
<html lang="en">
<head>
<meta charset="utf-8">
<title>The Maple Lectern — Business Card</title>
<link rel="stylesheet" href="https://fonts.googleapis.com/css2?family=Righteous&family=Arimo:wght@400&display=swap">
<style>
  :root {
    --backdrop-light: #e6e6e6;
    --backdrop-dark: #a9a9a9;
    --card-black: #0b0b0d;
    --front-navy: #0d1a4a;
    --front-blue: #1f3f9a;
    --brand-cyan: #3fe3f2;
    --band-white: #ffffff;
    --info-grey: #d4d4d4;
    --label-ink: #1a1a1a;
  }
  * { margin: 0; padding: 0; box-sizing: border-box; }
  html, body { width: 1200px; height: 450px; overflow: hidden; }
  body {
    position: relative;
    background: radial-gradient(ellipse at 50% 40%, var(--backdrop-light) 0%, var(--backdrop-dark) 100%);
    font-family: "Arimo", Arial, sans-serif;
  }
  .card {
    position: absolute;
    top: 92px;
    width: 525px;
    height: 300px;
    border-radius: 20px;
    overflow: hidden;
    background: var(--card-black);
  }
  .card--front { left: 66px; }
  .card--back { left: 605px; }

  .front-art {
    position: absolute;
    inset: 0 125px 0 0;
    background: radial-gradient(ellipse at 35% 45%, var(--front-blue) 0%, var(--front-navy) 55%, var(--card-black) 100%);
  }
  .front-stripes {
    position: absolute;
    top: 0; right: 0; bottom: 0;
    width: 125px;
    background: linear-gradient(90deg, #202226 0%, #8a8c90 55%, #3a3c40 100%);
  }
  .front-brand {
    position: absolute;
    left: 72px;
    top: 92px;
    display: flex;
    align-items: center;
    gap: 14px;
  }
  .brand-dot {
    width: 96px; height: 96px;
    border-radius: 50%;
    background: var(--brand-cyan);
    border: 6px solid var(--card-black);
    flex: none;
  }
  .brand-name {
    font-family: "Righteous", "Arial Black", sans-serif;
    font-weight: 400;
    color: var(--brand-cyan);
    text-transform: uppercase;
    line-height: 1.05;
    letter-spacing: 1px;
  }
  .front-brand .brand-name {
    font-size: 38px;
    background: var(--card-black);
    padding: 6px 12px;
  }

  .back-band {
    position: absolute;
    left: 0; right: 0;
    top: 76px;
    height: 78px;
    background: var(--band-white);
    display: flex;
    align-items: center;
    justify-content: center;
    gap: 12px;
  }
  .back-band .brand-dot {
    width: 60px; height: 60px;
    border: none;
    background: #2b6fd8;
  }
  .back-band .brand-name { font-size: 26px; color: #26c7e6; }

  .social-row {
    position: absolute;
    top: 174px;
    left: 0; right: 0;
    display: flex;
    justify-content: center;
    gap: 14px;
    list-style: none;
    font-size: 10px;
    color: var(--info-grey);
  }
  .social-row li { display: flex; align-items: center; gap: 5px; }
  .social-square { width: 9px; height: 9px; background: var(--info-grey); display: inline-block; }

  .side-label {
    position: absolute;
    top: 400px;
    left: 0; right: 0;
    text-align: center;
    font-size: 13px;
    font-weight: 700;
    color: var(--label-ink);
    letter-spacing: 1px;
    word-spacing: 14px;
  }
</style>
</head>
<body>
  <section class="card card--front" aria-label="Card front">
    <div class="front-art" role="img" aria-label="Dark blue world map backdrop"></div>
    <div class="front-stripes" role="img" aria-label="Vertical silver stripe pattern"></div>
    <div class="front-brand">
      <span class="brand-dot"></span>
      <span class="brand-name">The Maple<br>Lectern</span>
    </div>
  </section>

  <section class="card card--back" aria-label="Card back">
    <div class="back-band">
      <span class="brand-dot"></span>
      <span class="brand-name">The Maple<br>Lectern</span>
    </div>
    <ul class="social-row">
      <li><span class="social-square"></span>friendsphere.com/maplelectern</li>
      <li><span class="social-square"></span>www.talkwave.com/maplelectern</li>
      <li><span class="social-square"></span>chirpline.com/maplelectern</li>
    </ul>
  </section>

  <p class="side-label">FRONT // BACK</p>
</body>
</html>
```